Re-design of Business Card

We require a design for our business card.

Quorin is a supplier of industrial packaging specializing in plastic products. We are undergoing a rebranding to appear more corporate. We have changed our company name to quorin and have a new logo.

I have uploaded our old card design with the previous company name.
Don't copy the current design. We are looking for a new design.

Industry/Entity Type

Manufacturing

Contact Information for Business Card

please don't copy the current design. we are looking for a new design.

Font styles to use
Sans Serif

Colors

Designer to choose colors to be used in the design.

Requirements
Must have
• clean and easy to read.

```html
<!DOCTYPE html>
<html lang="en">
<head>
<meta charset="utf-8">
<title>Quorin Business Card</title>
<link href="https://fonts.googleapis.com/css2?family=Arimo:ital,wght@0,400;0,700;1,700&display=swap" rel="stylesheet">
<style>
  :root {
    --orange: #f37f20;
    --charcoal: #4d4d4f;
    --text: #4a4a4a;
    --paper: #ffffff;
    --trim: #f2a0a0;
  }
  * { margin: 0; padding: 0; box-sizing: border-box; }
  html, body { width: 1200px; height: 1000px; overflow: hidden; background: var(--paper); }
  body { position: relative; font-family: "Arimo", Arial, sans-serif; color: var(--text); }

  .card { position: absolute; left: 265px; width: 670px; height: 410px; border: 1px solid var(--trim); background: var(--paper); overflow: hidden; }
  .card--front { top: 57px; }
  .card--back { top: 533px; }
  .card > * { position: absolute; }

  .band { left: 0; bottom: 0; width: 670px; height: 50px; }
  .band-url { left: 0; width: 650px; bottom: 15px; text-align: center; color: #fff; font-size: 24px; }

  .brand-name { left: 25px; top: 30px; color: var(--orange); font-weight: 700; font-size: 66px; letter-spacing: 1px; line-height: 1; }

  .address { left: 57px; top: 200px; font-size: 20px; line-height: 25px; }
  .pin { left: 32px; top: 204px; }

  .person { right: 24px; top: 200px; text-align: right; font-size: 22px; line-height: 28px; }
  .person-name { font-weight: 700; font-style: italic; font-size: 30px; line-height: 36px; color: var(--charcoal); letter-spacing: 0.5px; }

  .seal { left: 24px; }

  .services { right: 24px; top: 19px; width: 300px; text-align: right; font-size: 17px; line-height: 20px; color: var(--text); }
  .service-tab { display: block; margin-left: auto; height: 23px; background: var(--orange); color: #fff; font-weight: 700; font-size: 18px; line-height: 23px; padding-right: 10px; clip-path: polygon(12px 0, 100% 0, 100% 100%, 0 100%); }
  .service-tab--short { width: 212px; }
  .service-tab--long { width: 282px; }
  .service-group + .service-group { margin-top: 4px; }
  .service-items { padding-top: 1px; }
</style>
</head>
<body>

<section class="card card--front">
  <div class="brand-name">QUORIN</div>

  <svg class="pin" width="20" height="20" viewBox="0 0 20 20" aria-hidden="true">
    <circle cx="10" cy="10" r="10" fill="var(--orange)"/>
    <path d="M10 4.5a3.6 3.6 0 0 0-3.6 3.6c0 2.6 3.6 6.8 3.6 6.8s3.6-4.2 3.6-6.8A3.6 3.6 0 0 0 10 4.5z" fill="#fff"/>
    <circle cx="10" cy="8.1" r="1.4" fill="var(--orange)"/>
  </svg>
  <address class="address" style="font-style:normal">
    Head Office<br>
    48, Marlow Rd.<br>
    Westbrook Hts, Qld<br>
    4210, Australia<br>
    Tel.: 1300 418 206<br>
    Mob.: +61 7 3054 7219
  </address>

  <div class="person">
    <div class="person-name">Darian Holt</div>
    <div>Machinery Sales Manager</div>
    <div>01234 908 315</div>
    <div>darian@quorin.co.au</div>
  </div>

  <svg class="band" viewBox="0 0 670 50" aria-hidden="true">
    <polygon points="0,0 525,0 575,50 0,50" fill="var(--orange)"/>
    <polygon points="543,0 670,0 670,50 593,50" fill="var(--charcoal)"/>
  </svg>
  <div class="band-url">www.quorin.co.au</div>
</section>

<section class="card card--back">
  <svg class="seal" style="top:26px" width="100" height="100" viewBox="0 0 100 100" role="img" aria-label="Distribution badge">
    <circle cx="50" cy="50" r="48" fill="var(--orange)"/>
    <circle cx="50" cy="50" r="38" fill="#fff"/>
  </svg>
  <svg class="seal" style="top:130px" width="100" height="100" viewBox="0 0 100 100" role="img" aria-label="Food safety certification badge">
    <circle cx="50" cy="50" r="48" fill="var(--orange)"/>
    <circle cx="50" cy="50" r="38" fill="#fff"/>
  </svg>
  <svg class="seal" style="top:234px" width="100" height="100" viewBox="0 0 100 100" role="img" aria-label="Quality standard certification badge">
    <circle cx="50" cy="50" r="48" fill="var(--orange)"/>
    <circle cx="50" cy="50" r="38" fill="#fff"/>
  </svg>

  <div class="services">
    <div class="service-group">
      <span class="service-tab service-tab--short">Pallet Containment</span>
      <div class="service-items">Stretch<br>Heat Shrink<br>Pallet Hood</div>
    </div>
    <div class="service-group">
      <span class="service-tab service-tab--short">Flexible Packaging</span>
      <div class="service-items">Bags &amp; Liners<br>Tube<br>Film &amp; Sheet<br>Printed Films ( 12 col)<br>Shrink Films</div>
    </div>
    <div class="service-group">
      <span class="service-tab service-tab--long">Pallet Wrapping Machinery</span>
      <div class="service-items">Semi &amp; Fully Auto Lines<br>finance options include Lease, Rent<br>pay per wrap</div>
    </div>
    <div class="service-group">
      <span class="service-tab service-tab--long">General Packaging</span>
    </div>
  </div>

  <svg class="band" viewBox="0 0 670 50" aria-hidden="true">
    <polygon points="0,0 128,0 78,50 0,50" fill="var(--charcoal)"/>
    <polygon points="145,0 670,0 670,50 95,50" fill="var(--orange)"/>
  </svg>
  <div class="band-url">www.quorin.co.au</div>
</section>

</body>
</html>
```